I'm a magician . hypnotist also a good barber. I need this all to be shown in good detail on the cards.

Industry/Entity Type

Magician

Contact Information for Business Card

Magician/ hypnotist/barber Rowan Pitt. One of the best. Tel 07421 736204
Email.Trickshears48@fernmail.example
Title of card spell chap.

```html
<!DOCTYPE html>
<html lang="en">
<head>
<meta charset="utf-8">
<title>Spell Chap – Rowan Pitt</title>
<link rel="stylesheet" href="https://fonts.googleapis.com/css2?family=Bodoni+Moda:wght@500&family=Open+Sans:wght@400;700&display=swap">
<style>
  :root {
    --gold: #edb52e;
    --ink: #111111;
    --paper: #ffffff;
  }
  * { margin: 0; padding: 0; box-sizing: border-box; }
  html, body { width: 1200px; height: 791px; overflow: hidden; background: var(--paper); }
  .card {
    position: relative;
    width: 1200px;
    height: 791px;
    background: var(--paper);
    font-family: "Open Sans", Arial, sans-serif;
    color: var(--ink);
    overflow: hidden;
  }
  .side-band {
    position: absolute; left: 0; top: 0;
    width: 181px; height: 791px;
    background: var(--gold);
  }
  .side-stripe {
    position: absolute; left: 190px; top: 0;
    width: 23px; height: 791px;
    background: var(--gold);
  }
  .side-text {
    position: absolute; left: 0; top: 0;
    width: 791px; height: 181px;
    transform-origin: 0 0;
    transform: translate(0, 791px) rotate(-90deg);
  }
  .brand-title {
    position: absolute;
    left: 35px; top: 18px;
    width: 721px;
    font-family: "Bodoni Moda", "Times New Roman", serif;
    font-weight: 500;
    font-size: 118px;
    line-height: 110px;
    color: var(--paper);
    text-transform: uppercase;
    white-space: nowrap;
    display: flex;
    justify-content: space-between;
  }
  .contact-email {
    position: absolute;
    left: 133px; top: 132px;
    width: 525px;
    font-size: 24px;
    line-height: 34px;
    color: var(--ink);
    white-space: nowrap;
    text-align: center;
  }
  .owner-name, .owner-phone {
    position: absolute;
    top: 32px;
    font-weight: 700;
    font-size: 30px;
    line-height: 40px;
  }
  .owner-name { left: 252px; }
  .owner-phone { right: 32px; }
  .service {
    position: absolute;
    top: 278px;
    width: 240px;
    text-align: center;
  }
  .service svg { display: block; margin: 0 auto; height: 160px; }
  .service-label {
    margin-top: 18px;
    font-weight: 700;
    font-size: 32px;
    line-height: 40px;
    letter-spacing: 0.3px;
  }
  .service--magician { left: 275px; }
  .service--barber { left: 588px; }
  .service--hypnotist { left: 887px; }
</style>
</head>
<body>
<main class="card">
  <div class="side-band"></div>
  <div class="side-stripe"></div>
  <div class="side-text">
    <h1 class="brand-title"><span>S</span><span>P</span><span>E</span><span>L</span><span>L</span><span>&nbsp;</span><span>C</span><span>H</span><span>A</span><span>P</span></h1>
    <p class="contact-email">Email: Trickshears48@fernmail.example</p>
  </div>

  <p class="owner-name">ROWAN PITT</p>
  <p class="owner-phone">TEL: 07421 736204</p>

  <section class="service service--magician">
    <svg viewBox="0 0 140 160" aria-hidden="true">
      <ellipse cx="70" cy="120" rx="67" ry="32" fill="var(--gold)"/>
      <path d="M18 14 Q70 2 122 14 L118 132 Q70 146 22 132 Z" fill="var(--gold)"/>
      <path d="M40 30 Q70 40 100 30" stroke="var(--paper)" stroke-width="5" fill="none" stroke-linecap="round"/>
      <path d="M22 132 Q70 150 118 132" stroke="var(--paper)" stroke-width="4" fill="none" stroke-linecap="round"/>
    </svg>
    <p class="service-label">MAGICIAN</p>
  </section>

  <section class="service service--barber">
    <svg viewBox="0 0 130 160" aria-hidden="true">
      <circle cx="14" cy="10" r="9" fill="var(--gold)"/>
      <path d="M38 62 L110 156 L96 160 L30 72 Z" fill="var(--gold)"/>
      <path d="M92 62 L20 156 L26 124 L100 72 Z" fill="var(--gold)"/>
      <circle cx="30" cy="40" r="26" fill="var(--gold)"/>
      <circle cx="100" cy="40" r="26" fill="var(--gold)"/>
      <circle cx="30" cy="40" r="11" fill="var(--paper)"/>
      <circle cx="100" cy="40" r="11" fill="var(--paper)"/>
      <circle cx="65" cy="96" r="5" fill="var(--paper)"/>
    </svg>
    <p class="service-label">BARBER</p>
  </section>

  <section class="service service--hypnotist">
    <svg viewBox="0 0 160 160" aria-hidden="true">
      <circle cx="80" cy="80" r="78" fill="var(--gold)"/>
      <g fill="none" stroke="var(--paper)">
        <circle cx="80" cy="80" r="62" stroke-width="5"/>
        <circle cx="80" cy="80" r="50" stroke-width="4"/>
        <circle cx="80" cy="80" r="40" stroke-width="3.5"/>
        <circle cx="80" cy="80" r="31" stroke-width="3"/>
        <circle cx="80" cy="80" r="23" stroke-width="2.5"/>
        <circle cx="80" cy="80" r="16" stroke-width="2"/>
        <circle cx="80" cy="80" r="10" stroke-width="1.6"/>
        <circle cx="80" cy="80" r="5" stroke-width="1.2"/>
      </g>
    </svg>
    <p class="service-label">HYPNOTIST</p>
  </section>
</main>
</body>
</html>
```